eCommerce website for the sale of vehicle tyres

We need the design of a logo and website for an ecommerce website that sells tyres to vehicle owners.

Users to the website should be able to search brand of tyre, type of tyre and make payment online.

The website should have algorithm to calculate delivery price based on user location and include in total price payable by CoinLark or SwiftTill.

Multi-language website (5 languages)
Content for website available in attached brief.

Number of pages:
1. Home page (with slider on how it works and search area)
2. Search results page
3. About Us page
4. Contact Us page

Target Market(s)

Owners of vehicles

Industry/Entity Type

Automotive

Logo Text

Vorel

Coding

Coded - Design and coding required

Number of Pages Required

5+ page

Font styles to use
Serif

Colors
0255a3
9d9d9d
ec1f27

Requirements
Must have
• Clean design
• Search feature on front page
Should not have
• Complicated

```html
<!DOCTYPE html>
<html lang="en">
<head>
<meta charset="utf-8">
<title>Vorel – Wheels &amp; Tyres</title>
<link href="https://fonts.googleapis.com/css2?family=Titillium+Web:wght@400;600;700&family=Open+Sans:wght@400;600;700&display=swap" rel="stylesheet">
<style>
:root{
  --red:#ec1f27;
  --blue:#0255a3;
  --grey:#9d9d9d;
  --ink:#1e1e1e;
  --charcoal:#2b2b2b;
  --soft:#f2f2f2;
  --line:#dcdcdc;
  --white:#ffffff;
}
*{box-sizing:border-box;margin:0;padding:0}
html,body{width:1200px;height:2644px;overflow:hidden}
body{font-family:"Open Sans",Arial,sans-serif;color:var(--ink);background:var(--white);font-size:14px}
.wrap{width:1056px;margin:0 auto;position:relative}
h1,h2,h3{font-family:"Titillium Web",Arial,sans-serif}

/* header */
.site-header{height:112px;background:var(--white)}
.site-header .wrap{height:112px;display:flex;align-items:center;justify-content:space-between}
.brand{display:flex;align-items:center;gap:10px;font-family:"Titillium Web",sans-serif;font-weight:700;font-size:46px;color:var(--ink);letter-spacing:-1px}
.brand-square{width:14px;height:14px;background:var(--red)}
.search{display:flex;width:430px;height:40px;border:1px solid var(--line);margin-left:80px}
.search input{flex:1;border:0;padding:0 14px;font:13px "Open Sans",sans-serif;color:var(--grey)}
.search button{width:46px;border:0;background:var(--red);display:flex;align-items:center;justify-content:center}
.account{display:flex;flex-direction:column;align-items:flex-end;gap:8px;font-size:13px}
.cart{display:flex;flex-direction:column;align-items:center;background:var(--ink);color:var(--white);width:52px;height:46px;justify-content:center;font-size:11px;font-weight:700}
.account-links{display:flex;gap:22px}
.account-links span{display:flex;align-items:center;gap:6px}
.account-links span::before{content:"";width:6px;height:6px;background:var(--red);border-radius:50%}

/* nav */
.main-nav{background:var(--red);height:60px}
.main-nav .wrap{display:flex;height:60px;align-items:center}
.categories{background:var(--charcoal);color:var(--white);height:60px;width:190px;display:flex;align-items:center;justify-content:center;gap:12px;font-weight:700;font-size:14px;letter-spacing:.5px}
.nav-links{display:flex;list-style:none;margin-left:60px;gap:62px;color:var(--white);font-size:14px;font-weight:600;text-transform:uppercase}

/* hero */
.hero{height:488px;position:relative;background:radial-gradient(ellipse at 75% 40%,#5a5a5a 0%,#2a2a2a 45%,#141414 100%);display:flex;flex-direction:column;align-items:center;justify-content:center;text-align:center}
.hero h1{color:var(--white);font-size:64px;font-weight:700;letter-spacing:2px;line-height:1}
.hero p{color:var(--red);font-family:"Titillium Web",sans-serif;font-size:48px;font-weight:600;letter-spacing:1px;margin-top:6px}

/* promos */
.promos{padding:40px 0}
.promos .wrap{display:flex;gap:24px}
.promo{flex:1;height:104px;display:flex;align-items:center;padding:0 24px;border:1px solid var(--line);position:relative;overflow:hidden}
.promo .big{font-family:"Titillium Web",sans-serif;font-weight:700;font-size:42px;line-height:.95;color:var(--ink)}
.promo .big em{font-style:normal;color:var(--red)}
.promo .small{font-size:13px;font-weight:700;text-transform:uppercase;line-height:1.2}
.promo .thumb{position:absolute;right:14px;top:12px;width:100px;height:80px;border-radius:50%;background:radial-gradient(circle,#666 0%,#222 55%,#111 70%)}
.promo-shipping{background:var(--red);border-color:var(--red);color:var(--white);flex-direction:column;justify-content:center;text-align:center}
.promo-shipping .big{color:var(--white);font-size:40px}
.promo-shipping .small{color:var(--white)}

/* featured */
.section-bar{height:60px;background:var(--red);display:flex;align-items:center;justify-content:space-between;padding:0 20px;margin-top:20px}
.section-bar h2{color:var(--white);font-size:26px;font-weight:700;letter-spacing:1px}
.view-toggle{display:flex;gap:8px}
.view-toggle span{width:36px;height:36px;background:var(--white);display:flex;align-items:center;justify-content:center}
.products{display:grid;grid-template-columns:repeat(4,1fr);gap:40px 24px;margin-top:40px}
.product{border:1px solid var(--line);height:340px;display:flex;flex-direction:column}
.product-photo{height:178px;margin:14px;background:radial-gradient(circle at 50% 50%,#7a7a7a 0%,#3b3b3b 30%,#111 55%,#fff 57%)}
.product-name{padding:6px 14px;font-size:12px;color:#555;line-height:1.4}
.product.highlight .product-name{background:var(--red);color:var(--white)}
.price{padding:6px 14px;font-size:14px;font-weight:700;color:var(--red)}
.price s{color:var(--grey);font-weight:400;font-size:12px;margin-left:8px}
.actions{display:flex;justify-content:space-between;padding:6px 14px}
.btn{height:30px;padding:0 14px;font-size:11px;display:flex;align-items:center;font-weight:600}
.btn-cart{background:var(--red);color:var(--white)}
.btn-details{border:1px solid var(--line);color:#555;gap:14px}

/* services */
.services{margin-top:40px;height:420px;background:linear-gradient(100deg,#1b1b1b 0%,#2c2c2c 55%,#3d3d3d 100%);color:var(--white);padding-top:40px}
.services h2{font-size:52px;font-weight:700;letter-spacing:1px;line-height:1}
.services h2 span{color:var(--red)}
.service-grid{display:grid;grid-template-columns:1fr 1fr;gap:42px 60px;margin-top:34px}
.service{display:flex;gap:22px}
.service .num{flex:none;width:78px;height:78px;background:var(--red);display:flex;align-items:center;justify-content:center;font-family:"Titillium Web",sans-serif;font-size:36px;font-weight:700}
.service h3{font-size:16px;font-weight:700;text-transform:uppercase;letter-spacing:.5px}
.service p{font-size:13px;line-height:1.5;color:#cfcfcf;margin-top:6px;max-width:380px}

/* brands */
.brands{background:var(--soft);height:180px;display:flex;align-items:center}
.brands .wrap{display:flex;gap:24px}
.brand-tile{flex:1;height:96px;background:var(--white);border:1px solid var(--line);display:flex;align-items:center;justify-content:center;font-family:"Titillium Web",sans-serif;font-weight:700;font-size:22px;color:var(--ink);text-transform:uppercase;letter-spacing:1px}

/* footer */
.site-footer{padding-top:30px;height:204px}
.footer-cols{display:grid;grid-template-columns:repeat(4,1fr) 1.1fr;gap:20px}
.footer-cols h4{font-size:14px;font-weight:700;text-transform:uppercase;margin-bottom:10px}
.footer-cols ul{list-style:none;font-size:12px;color:#666;line-height:1.9}
.footer-cols li::before{content:"›";color:var(--red);margin-right:6px}
.social{display:flex;gap:12px}
.social span{width:42px;height:42px;background:var(--red)}
.trust-bar{height:64px;border-top:1px solid var(--line)}
.trust-bar .wrap{height:64px;display:flex;align-items:center;gap:36px}
.trust{display:flex;align-items:center;gap:10px;font-size:11px;font-weight:700;text-transform:uppercase;line-height:1.25}
.trust-icon{width:34px;height:34px;border-radius:50%;background:var(--red);display:flex;align-items:center;justify-content:center}
.copyright{margin-left:auto;font-size:11px;color:#777}
</style>
</head>
<body>

<header class="site-header">
  <div class="wrap">
    <div class="brand"><span class="brand-square"></span>Vorel</div>
    <form class="search">
      <input type="text" value="Search your tyres here">
      <button type="button" aria-label="Search">
        <svg width="18" height="18" viewBox="0 0 18 18"><circle cx="7.5" cy="7.5" r="5.5" fill="none" stroke="#fff" stroke-width="2"/><line x1="11.5" y1="11.5" x2="16" y2="16" stroke="#fff" stroke-width="2"/></svg>
      </button>
    </form>
    <div class="account">
      <div class="cart">
        <svg width="20" height="16" viewBox="0 0 20 16"><path d="M1 1h3l2 10h11l2-7H5" fill="none" stroke="#fff" stroke-width="1.6"/><circle cx="8" cy="14" r="1.4" fill="#fff"/><circle cx="15" cy="14" r="1.4" fill="#fff"/></svg>
        CART
      </div>
      <div class="account-links"><span>Create an Account</span><span>Log in</span></div>
    </div>
  </div>
</header>

<nav class="main-nav">
  <div class="wrap">
    <div class="categories">CATEGORIES
      <svg width="18" height="14" viewBox="0 0 18 14"><rect width="18" height="2" fill="#fff"/><rect y="6" width="18" height="2" fill="#fff"/><rect y="12" width="18" height="2" fill="#fff"/></svg>
    </div>
    <ul class="nav-links">
      <li>Home</li><li>Car Tyres</li><li>Bike Tyres</li><li>Alloy Wheels</li><li>About Us</li><li>Contact Us</li>
    </ul>
  </div>
</nav>

<section class="hero" role="img" aria-label="Dark close-up photograph of a car wheel and tyre">
  <h1>FIND WHEELS &amp; TYRES</h1>
  <p>FOR ALL VEHICLE TYPES</p>
</section>

<section class="promos">
  <div class="wrap">
    <div class="promo">
      <div><div class="small">Get</div><div class="big"><em>40%</em>OFF</div></div>
      <div class="thumb" role="img" aria-label="Alloy wheel photo"></div>
    </div>
    <div class="promo">
      <div><div class="big">SAVE <em>10%</em></div><div class="small">When you use your<br>credit card</div></div>
      <div class="thumb" role="img" aria-label="Tyre photo"></div>
    </div>
    <div class="promo promo-shipping">
      <div class="big">FREE SHIPPING</div>
      <div class="small">On orders over $ 100</div>
    </div>
  </div>
</section>

<main class="wrap">
  <div class="section-bar">
    <h2>FEATURED PRODUCTS</h2>
    <div class="view-toggle">
      <span><svg width="18" height="16" viewBox="0 0 18 16"><rect width="18" height="3" fill="#ec1f27"/><rect y="6.5" width="18" height="3" fill="#ec1f27"/><rect y="13" width="18" height="3" fill="#ec1f27"/></svg></span>
      <span><svg width="16" height="16" viewBox="0 0 16 16"><rect width="7" height="7" fill="#ec1f27"/><rect x="9" width="7" height="7" fill="#ec1f27"/><rect y="9" width="7" height="7" fill="#ec1f27"/><rect x="9" y="9" width="7" height="7" fill="#ec1f27"/></svg></span>
    </div>
  </div>

  <div class="products">
    <article class="product highlight"><div class="product-photo" role="img" aria-label="Black tyre on alloy wheel"></div><div class="product-name">Ridgeline Velocita<br>VX420T</div><div class="price">$29.99<s>$39.99</s></div><div class="actions"><span class="btn btn-cart">Add to cart</span><span class="btn btn-details">Details ›</span></div></article>
    <article class="product"><div class="product-photo" role="img" aria-label="Black tyre on alloy wheel"></div><div class="product-name">Ridgeline Velocita<br>VX420T</div><div class="price">$29.99<s>$39.99</s></div><div class="actions"><span class="btn btn-cart">Add to cart</span><span class="btn btn-details">Details ›</span></div></article>
    <article class="product"><div class="product-photo" role="img" aria-label="Black tyre on alloy wheel"></div><div class="product-name">Ridgeline Velocita<br>VX420T</div><div class="price">$29.99<s>$39.99</s></div><div class="actions"><span class="btn btn-cart">Add to cart</span><span class="btn btn-details">Details ›</span></div></article>
    <article class="product"><div class="product-photo" role="img" aria-label="Black tyre on alloy wheel"></div><div class="product-name">Ridgeline Velocita<br>VX420T</div><div class="price">$29.99<s>$39.99</s></div><div class="actions"><span class="btn btn-cart">Add to cart</span><span class="btn btn-details">Details ›</span></div></article>
    <article class="product"><div class="product-photo" role="img" aria-label="Black tyre on alloy wheel"></div><div class="product-name">Ridgeline Velocita<br>VX420T</div><div class="price">$29.99<s>$39.99</s></div><div class="actions"><span class="btn btn-cart">Add to cart</span><span class="btn btn-details">Details ›</span></div></article>
    <article class="product"><div class="product-photo" role="img" aria-label="Black tyre on alloy wheel"></div><div class="product-name">Ridgeline Velocita<br>VX420T</div><div class="price">$29.99<s>$39.99</s></div><div class="actions"><span class="btn btn-cart">Add to cart</span><span class="btn btn-details">Details ›</span></div></article>
    <article class="product"><div class="product-photo" role="img" aria-label="Black tyre on alloy wheel"></div><div class="product-name">Ridgeline Velocita<br>VX420T</div><div class="price">$29.99<s>$39.99</s></div><div class="actions"><span class="btn btn-cart">Add to cart</span><span class="btn btn-details">Details ›</span></div></article>
    <article class="product"><div class="product-photo" role="img" aria-label="Black tyre on alloy wheel"></div><div class="product-name">Ridgeline Velocita<br>VX420T</div><div class="price">$29.99<s>$39.99</s></div><div class="actions"><span class="btn btn-cart">Add to cart</span><span class="btn btn-details">Details ›</span></div></article>
  </div>
</main>

<section class="services" role="img" aria-label="Dark background photograph of a car wheel">
  <div class="wrap">
    <h2>OUR <span>SERVICES</span></h2>
    <div class="service-grid">
      <div class="service"><div class="num">1</div><div><h3>Lorem ipsum is simply dummy text</h3><p>The printing and typesetting industry. Lorem Ipsum has been the industry's standard dummy text ever since the 1500s.</p></div></div>
      <div class="service"><div class="num">2</div><div><h3>Lorem ipsum is simply dummy text</h3><p>The printing and typesetting industry. Lorem Ipsum has been the industry's standard dummy text ever since the 1500s.</p></div></div>
      <div class="service"><div class="num">3</div><div><h3>Lorem ipsum is simply dummy text</h3><p>The printing and typesetting industry. Lorem Ipsum has been the industry's standard dummy text ever since the 1500s.</p></div></div>
      <div class="service"><div class="num">4</div><div><h3>Lorem ipsum is simply dummy text</h3><p>The printing and typesetting industry. Lorem Ipsum has been the industry's standard dummy text ever since the 1500s.</p></div></div>
    </div>
  </div>
</section>

<section class="brands">
  <div class="wrap">
    <div class="brand-tile">Dunmore</div>
    <div class="brand-tile">Yamaro</div>
    <div class="brand-tile">Castrelle</div>
    <div class="brand-tile">Pirano</div>
    <div class="brand-tile">Mirelle</div>
    <div class="brand-tile">Ridgeline</div>
  </div>
</section>

<footer>
  <div class="site-footer">
    <div class="wrap footer-cols">
      <div><h4>Main Menu</h4><ul><li>Home</li><li>What's New?</li><li>Featured</li><li>Top sellers</li></ul></div>
      <div><h4>Extras</h4><ul><li>Specials</li><li>Brands</li><li>Reviews</li></ul></div>
      <div><h4>Information</h4><ul><li>Privacy Policy</li><li>Contacts</li><li>Terms &amp; Conditions</li><li>Sitemap</li></ul></div>
      <div><h4>Your Account</h4><ul><li>Shipping &amp; Returns</li><li>Advanced Search</li><li>Create an Account</li><li>Log In</li></ul></div>
      <div><h4>Follow Us On</h4><div class="social"><span></span><span></span><span></span></div></div>
    </div>
  </div>
  <div class="trust-bar">
    <div class="wrap">
      <div class="trust"><span class="trust-icon"><svg width="16" height="14" viewBox="0 0 16 14"><path d="M1 7l5 5 9-10" fill="none" stroke="#fff" stroke-width="2.2"/></svg></span>Satisfaction<br>100% guaranteed</div>
      <div class="trust"><span class="trust-icon"><svg width="18" height="12" viewBox="0 0 18 12"><rect x="0" y="1" width="11" height="8" fill="#fff"/><path d="M11 4h4l3 3v2h-7z" fill="#fff"/><circle cx="4" cy="10.5" r="1.5" fill="#fff"/><circle cx="14" cy="10.5" r="1.5" fill="#fff"/></svg></span>Free shipping<br>on orders over $99</div>
      <div class="trust"><span class="trust-icon"><svg width="16" height="16" viewBox="0 0 16 16"><path d="M13 8a5 5 0 1 1-2-4" fill="none" stroke="#fff" stroke-width="2"/><path d="M9 1l3 3-3 2" fill="#fff"/></svg></span>7 day<br>easy returns</div>
      <div class="copyright">Copyright © 2019 Vorel. All Rights Reserved</div>
    </div>
  </div>
</footer>

</body>
</html>
```